Brightford Lingua Partners, LLC

We need a business card that includes information about our business and conveys a reliable business that provides document translation services and interpreters for a variety of corporate and individual clients. We want to come across as professional, reliable, yet approachable. It should include the following on one side:

ESL / ENL Language Classes, Private Lessons, and Online Tutors
PALQE Training and Testing
Translating & Interpreting Services
Contact us about Over-the-Phone Interpreting in over 200 languages
24/7/365
www.brightfordlingua.example

The other side should include (555) 481-3062

Marla Quennick, President
412 Garvin Ave., Ste. 209
Indianapolis, IN 46999
Updates

Please add USA as part of the address. Also, please add mrqquennick@brightfordlinguapartners.example as the e-mail address. Thank you.

Target Market(s)

Business professionals, their families, the international community

Industry/Entity Type

Business

Contact Information for Business Card

24/7/365
www.brightfordlingua.example

(555) 481-3062

Marla Quennick, President
412 Garvin Ave., Ste. 209
Indianapolis, IN 46999
USA

Font styles to use
Sans Serif

Colors

Designer to choose colors to be used in the design.

Requirements
Must have
• See project description
• e-mail address and web address
• Phone number
Nice to have
• a globe
• physical address
Should not have
• Should not have the same color scheme as other agencies in our market in Indiana unless it is blue and black. No purple or yellow.

```html
<!DOCTYPE html>
<html lang="en">
<head>
<meta charset="utf-8">
<title>Brightford Lingua Partners – Business Card</title>
<link href="https://fonts.googleapis.com/css2?family=Lato:wght@400;700&display=swap" rel="stylesheet">
<style>
  :root {
    --backdrop: #d2d3d5;
    --ink: #000000;
    --paper: #ffffff;
    --brand-blue: #2596d4;
    --globe-tone: #1c1715;
    --text-dark: #222222;
  }
  * { box-sizing: border-box; margin: 0; padding: 0; }
  html, body { width: 1200px; height: 1200px; overflow: hidden; }
  body {
    background: var(--backdrop);
    font-family: 'Lato', sans-serif;
    position: relative;
  }
  .card {
    position: absolute;
    overflow: hidden;
  }
  .card--front {
    left: 269px; top: 142px; width: 703px; height: 400px;
    background: var(--ink);
    color: var(--paper);
  }
  .card--back {
    left: 270px; top: 647px; width: 712px; height: 406px;
    background: var(--paper);
    color: var(--text-dark);
  }
  .globe-decoration {
    position: absolute;
    left: 147px; top: -12px; width: 400px; height: 400px;
    border-radius: 50%;
    background: radial-gradient(circle at 55% 40%, #221c19 0%, var(--globe-tone) 70%);
  }
  .wave { position: absolute; left: 0; bottom: 0; display: block; }

  .brand-mark {
    position: absolute;
    border-radius: 50%;
  }
  .card--front .brand-mark {
    left: 189px; top: 88px; width: 136px; height: 136px;
    background: var(--paper);
    border: 4px solid var(--ink);
    box-shadow: 0 0 0 3px var(--paper);
  }
  .card--back .brand-mark {
    left: 84px; top: 153px; width: 100px; height: 100px;
    background: var(--brand-blue);
  }
  .brand-name {
    position: absolute;
    font-weight: 400;
    white-space: nowrap;
  }
  .card--front .brand-name {
    left: 336px; top: 96px;
    font-size: 34px;
    line-height: 42px;
    color: var(--paper);
  }
  .card--back .brand-name {
    left: 192px; top: 155px;
    font-size: 24px;
    line-height: 32px;
    color: var(--text-dark);
  }

  .services {
    position: absolute;
    left: 0; right: 0; top: 250px;
    text-align: center;
    font-size: 13.5px;
    line-height: 16.6px;
    color: var(--paper);
  }

  .person {
    position: absolute;
    left: 384px; top: 132px;
  }
  .person__name {
    font-size: 26px; font-weight: 700;
    color: var(--brand-blue);
    line-height: 1.1;
  }
  .person__title {
    font-size: 19px;
    margin-left: 3px;
    line-height: 1.2;
  }
  .contact-icons {
    position: absolute;
    left: 348px; top: 205px; width: 17px; height: 88px;
    background: var(--ink);
    border-radius: 3px;
  }
  .contact-list {
    position: absolute;
    left: 384px; top: 206px;
    list-style: none;
    font-size: 14.5px;
    line-height: 17px;
  }
  .contact-list li { margin-bottom: 5.5px; }
  .contact-list .address { margin-top: 1px; }
</style>
</head>
<body>

<section class="card card--front" aria-label="Card front">
  <div class="globe-decoration" role="img" aria-label="Faint world globe decoration"></div>
  <div class="brand-mark"></div>
  <p class="brand-name">Brightford<br>Lingua<br>Partners LLC</p>
  <div class="services">
    <p>ESL / ENL Language Classes, Private Lessons, and Online Tutors</p>
    <p>PALQE Training and Testing</p>
    <p>Translating &amp; Interpreting Services</p>
    <p>Contact us about Over-the-Phone Interpreting in over 200 languages</p>
    <p>24/7/365</p>
  </div>
  <svg class="wave" width="703" height="60" viewBox="0 0 703 60" aria-hidden="true">
    <path d="M0,42 C110,10 200,0 300,4 C420,10 520,40 703,50 L703,60 L0,60Z" fill="var(--brand-blue)"/>
    <path d="M480,30 C560,36 640,34 703,12 L703,26 C650,44 570,46 500,38Z" fill="var(--brand-blue)"/>
    <path d="M470,32 C560,42 650,38 703,20 L703,28 C650,48 560,52 490,40Z" fill="var(--ink)"/>
  </svg>
</section>

<section class="card card--back" aria-label="Card back">
  <div class="brand-mark"></div>
  <p class="brand-name">Brightford<br>Lingua<br>Partners LLC</p>

  <div class="person">
    <p class="person__name">Marla Quennick</p>
    <p class="person__title">President</p>
  </div>

  <svg class="contact-icons" viewBox="0 0 17 88" aria-hidden="true">
    <path d="M5,6 l2,0 l1,3 l-1,1 q1,2 3,3 l1,-1 l3,1 l0,2 q-6,1 -9,-7z" fill="#fff"/>
    <text x="8.5" y="35" font-size="11" fill="#fff" text-anchor="middle" font-family="Lato, sans-serif">@</text>
    <path d="M6,60 l4,-4 M5,58 l2,-2 a1.5,1.5 0 0 1 2,2 M11,58 l-2,2 a1.5,1.5 0 0 1 -2,-2" stroke="#fff" stroke-width="1.2" fill="none"/>
    <path d="M8.5,84 c-3,-4 -4,-5.5 -4,-7.5 a4,4 0 0 1 8,0 c0,2 -1,3.5 -4,7.5z" fill="#fff"/>
    <circle cx="8.5" cy="76.5" r="1.5" fill="#000"/>
  </svg>

  <ul class="contact-list">
    <li>(555) 481-3062</li>
    <li>mrqquennick@brightfordlinguapartners.example</li>
    <li>www.brightfordlingua.example</li>
    <li class="address">412 Garvin Ave., Ste. 209<br>Indianapolis, IN 46999<br>USA</li>
  </ul>

  <svg class="wave" width="712" height="60" viewBox="0 0 712 60" aria-hidden="true">
    <path d="M0,42 C110,10 200,0 300,4 C420,10 520,40 712,50 L712,60 L0,60Z" fill="var(--brand-blue)"/>
    <path d="M480,30 C560,36 650,32 712,5 L712,22 C650,42 570,46 500,38Z" fill="var(--brand-blue)"/>
    <path d="M470,32 C560,42 650,36 712,17 L712,24 C650,46 560,50 490,40Z" fill="var(--paper)"/>
  </svg>
</section>

</body>
</html>
```